Orlenta needs a new design we have an updated logo and want a high qualitative high end feel

feel and aesthetic should be high qualitative like the packaging in a zuvi or the qualatative weight/feel of an zuvi design. modern, elegant bold.probably just the orlenta logo on the backone vesion could be blue background white letter ... open to ideas
Target Market(s)
legal, insurance , medical, finance rho 740
Industry/Entity Type
Information Technology
Font styles to use
Serif

```html
<!DOCTYPE html>
<html lang="en">
<head>
<meta charset="utf-8">
<title>Orlenta business card</title>
<link href="https://fonts.googleapis.com/css2?family=Roboto:wght@400;500&display=swap" rel="stylesheet">
<style>
  :root {
    --backdrop: #2c2d2f;
    --paper: #f3f3f3;
    --navy: #263a51;
    --ink: #1f2f45;
    --muted: #6f7277;
    --rule: #c9c9c9;
    --strip: #a9a9ab;
    --white: #ffffff;
  }
  * { margin: 0; padding: 0; box-sizing: border-box; }
  html, body {
    width: 1200px; height: 800px; overflow: hidden;
    background: var(--backdrop);
    font-family: "Roboto", Arial, sans-serif;
  }
  .canvas { position: relative; width: 1200px; height: 800px; }
  .card {
    position: absolute; left: 357px; width: 524px; height: 300px;
    overflow: hidden;
    box-shadow: 0 6px 14px rgba(0,0,0,0.45);
  }
  .card-front { top: 92px; background: var(--paper); }
  .card-back { top: 430px; background: var(--navy); }

  .wordmark {
    position: absolute; font-weight: 500; line-height: 1;
    letter-spacing: -0.5px; white-space: nowrap;
  }
  .card-front .wordmark { left: 40px; top: 128px; font-size: 50px; color: var(--ink); }
  .card-back .wordmark { left: 0; right: 0; top: 136px; font-size: 62px; text-align: center; color: var(--white); }

  .divider {
    position: absolute; left: 273px; top: 81px; width: 1px; height: 129px;
    background: var(--rule);
  }
  .contact { position: absolute; left: 296px; top: 78px; color: var(--muted); white-space: nowrap; }
  .contact-name { font-size: 19px; font-weight: 400; color: var(--ink); line-height: 1.2; }
  .contact-role { font-size: 13px; margin-top: 1px; }
  .contact-address { font-size: 15px; line-height: 18px; margin-top: 12px; }
  .contact-lines { margin-top: 11px; font-size: 16px; line-height: 19px; }
  .contact-line { display: flex; align-items: center; gap: 8px; }
  .contact-line svg { width: 13px; height: 13px; fill: var(--ink); }

  .edge-strip { position: absolute; left: 0; bottom: 0; width: 100%; height: 14px; }

  .website {
    position: absolute; left: 0; right: 0; top: 258px; text-align: center;
    color: var(--white); font-size: 15px; letter-spacing: 0.3px;
  }
</style>
</head>
<body>
<main class="canvas">
  <section class="card card-front">
    <div class="wordmark">orlenta</div>
    <div class="divider"></div>
    <div class="contact">
      <h1 class="contact-name">Daniel Hartley</h1>
      <p class="contact-role">Founder</p>
      <p class="contact-address">Eastbrook 218 Suite 405<br>Townsend Region CD457</p>
      <div class="contact-lines">
        <p class="contact-line">
          <svg viewBox="0 0 24 24" aria-hidden="true"><path d="M6.6 10.8a15.1 15.1 0 0 0 6.6 6.6l2.2-2.2c.3-.3.7-.4 1-.2 1.1.4 2.3.6 3.6.6.6 0 1 .4 1 1V20c0 .6-.4 1-1 1A17 17 0 0 1 3 4c0-.6.4-1 1-1h3.5c.6 0 1 .4 1 1 0 1.3.2 2.5.6 3.6.1.3 0 .7-.2 1z"/></svg>
          0371 4820 615
        </p>
        <p class="contact-line">
          <svg viewBox="0 0 24 24" aria-hidden="true"><path d="M2 5h20v14H2z M2 5l10 8 10-8" fill="none" stroke="#1f2f45" stroke-width="2"/></svg>
          info@orlenta.example
        </p>
      </div>
    </div>
    <svg class="edge-strip" viewBox="0 0 524 14" preserveAspectRatio="none" aria-hidden="true">
      <path d="M0 7 H266 L262 14 H0 Z" fill="var(--strip)"/>
      <path d="M262 14 Q268 2 284 2 H524 V14 Z" fill="var(--navy)"/>
    </svg>
  </section>

  <section class="card card-back">
    <div class="wordmark">orlenta</div>
    <p class="website">www.orlenta.example</p>
  </section>
</main>
</body>
</html>
```